R & T Summit Construction Business Card ideas

We want a business card to represents our company in a way that looks professional but is also a business card that is unique!

Industry/Entity Type

Construction Company

Contact Information for Business Card

open to all design ideas, just want to be able to see different options to choose from in either color or grayscale.

Requirements
Must have
• Our names and phone numbers
• Nolan Pritchett 512-804-2271
• Curtis Hale 512-693-1804
• Business logo

```html
<!DOCTYPE html>
<html lang="en">
<head>
<meta charset="utf-8">
<title>R &amp; T Summit Construction – Business Card</title>
<link rel="stylesheet" href="https://fonts.googleapis.com/css2?family=Lato:wght@400;700;900&display=swap">
<style>
  :root {
    --stage: #e4e2de;
    --card: #ffffff;
    --card-shade: #f1f1f1;
    --ink: #111111;
    --ink-soft: #2a2a2a;
    --ghost: #e9e9e9;
    --ghost-deep: #dedede;
  }
  * { box-sizing: border-box; margin: 0; padding: 0; }
  html, body {
    width: 1200px; height: 780px; overflow: hidden;
    background: var(--stage);
    font-family: "Lato", Arial, sans-serif;
    color: var(--ink);
  }
  .sheet {
    width: 1200px; height: 780px;
    display: flex; align-items: center; justify-content: center; gap: 40px;
  }
  .card {
    position: relative;
    width: 540px; height: 309px;
    background: linear-gradient(160deg, var(--card) 0%, var(--card) 55%, var(--card-shade) 100%);
    box-shadow: 0 2px 8px rgba(0,0,0,.18);
    overflow: hidden;
  }
  .card__backdrop {
    position: absolute; right: -40px; top: 20px;
    width: 330px; height: 300px;
    background: radial-gradient(ellipse at 55% 60%, var(--ghost-deep) 0%, var(--ghost) 45%, rgba(233,233,233,0) 75%);
  }
  .card__swoosh {
    position: absolute; inset: 0; width: 100%; height: 100%;
  }

  .brand {
    position: absolute;
    display: flex; flex-direction: column; align-items: stretch;
  }
  .brand__row {
    display: flex; align-items: center; gap: 10px;
    white-space: nowrap;
  }
  .brand__mark {
    width: 14px; height: 14px; flex: none; background: var(--ink);
  }
  .brand__name {
    font-weight: 900; text-transform: uppercase; letter-spacing: 1px;
    color: var(--ink); line-height: 1.1;
  }
  .brand__rule {
    height: 1px; background: var(--ink); margin-top: 8px; margin-left: 24px;
  }
  .card--front .brand { right: 32px; top: 62px; }
  .card--front .brand__name { font-size: 20px; }
  .card--back .brand { left: 50%; top: 50%; transform: translate(-50%, -50%); }
  .card--back .brand__name { font-size: 25px; }
  .card--back .brand__mark { width: 16px; height: 16px; }
  .card--back .brand__rule { margin-left: 26px; }

  .contact {
    position: absolute; left: 30px; bottom: 26px;
  }
  .contact__name {
    font-weight: 900; font-size: 18px; letter-spacing: .5px; text-transform: uppercase;
  }
  .contact__role {
    font-size: 13px; color: var(--ink-soft); margin-bottom: 12px;
  }
  .contact__line {
    display: flex; align-items: center; gap: 8px;
    font-size: 13px; line-height: 19px; color: var(--ink-soft);
  }
  .contact__icon {
    width: 16px; height: 16px; flex: none;
  }
  .contact__spacer { width: 16px; flex: none; }
</style>
</head>
<body>
<main class="sheet">

  <section class="card card--front" aria-label="Card front">
    <div class="card__backdrop" role="img" aria-label="Faint large rooftop decoration"></div>
    <svg class="card__swoosh" viewBox="0 0 540 309" aria-hidden="true">
      <path d="M250 309 C330 230 420 170 540 140 L540 158 C430 186 345 240 272 309 Z" fill="#ebebeb"/>
    </svg>

    <div class="brand">
      <div class="brand__row">
        <span class="brand__mark"></span>
        <span class="brand__name">R &amp; T Summit Construction</span>
      </div>
      <div class="brand__rule"></div>
    </div>

    <div class="contact">
      <p class="contact__name">Nolan Pritchett</p>
      <p class="contact__role">Director</p>
      <p class="contact__line"><span class="contact__spacer"></span>PO Box 418 Ridgeview Road</p>
      <p class="contact__line"><span class="contact__spacer"></span>Austin, TX, USA</p>
      <p class="contact__line">
        <svg class="contact__icon" viewBox="0 0 16 16" aria-hidden="true"><rect width="16" height="16" fill="#111"/><path d="M5 3.5h2l1 2.5-1.3 1a6 6 0 0 0 2.3 2.3l1-1.3 2.5 1v2a1 1 0 0 1-1 1A8.5 8.5 0 0 1 4 4.5a1 1 0 0 1 1-1z" fill="#fff"/></svg>
        512-804-2271
      </p>
      <p class="contact__line">
        <svg class="contact__icon" viewBox="0 0 16 16" aria-hidden="true"><rect width="16" height="16" fill="#111"/><rect x="3" y="4.5" width="10" height="7" fill="none" stroke="#fff" stroke-width="1.2"/><path d="M3 4.5l5 4 5-4" fill="none" stroke="#fff" stroke-width="1.2"/></svg>
        info@rtsummitbuild.com
      </p>
      <p class="contact__line">
        <svg class="contact__icon" viewBox="0 0 16 16" aria-hidden="true"><rect width="16" height="16" fill="#111"/><circle cx="8" cy="8" r="5" fill="none" stroke="#fff" stroke-width="1.1"/><ellipse cx="8" cy="8" rx="2.2" ry="5" fill="none" stroke="#fff" stroke-width="1"/><path d="M3 8h10" stroke="#fff" stroke-width="1"/></svg>
        www.rtsummitbuild.com
      </p>
    </div>
  </section>

  <section class="card card--back" aria-label="Card back">
    <div class="card__backdrop" role="img" aria-label="Faint large rooftop decoration"></div>
    <svg class="card__swoosh" viewBox="0 0 540 309" aria-hidden="true">
      <path d="M0 250 C120 200 260 190 420 220 L420 232 C260 204 120 214 0 266 Z" fill="#ececec"/>
    </svg>
    <div class="brand">
      <div class="brand__row">
        <span class="brand__mark"></span>
        <span class="brand__name">R &amp; T Summit Construction</span>
      </div>
      <div class="brand__rule"></div>
    </div>
  </section>

</main>
</body>
</html>
```